QORLIN Business card. A.I. company developing trading strategies.

My name is marcello bianchi and I'm CEO and co-founder of QORLIN Research, an AI company focusing on generating Ai-driven trading strategies.
This is our website: https://qorlin-analytics.example/
Values of our company: tech & R&D driven (we're all very mathy/stats/data driven), sophisticated (we only look for sophisticated, high knowledge investors), reserved (we don't go around telling anyone what we do).
Our main product: PivotFund. A trading strategy that delivered 70% in 2022 and 20% in 2023 so far.
Our main potential clients: HNW individuals, hedge funds, asset managers, tech entrepreneur.
Target Market(s)
Hedge funds, asset managers, High Net Worth individuals, Pension funds
Contact Information for Business Card
The basic: name, job title, company name, address, mail, phone number

```html
<!DOCTYPE html>
<html lang="en">
<head>
<meta charset="utf-8">
<title>QORLIN Research – Business Card</title>
<link rel="stylesheet" href="https://fonts.googleapis.com/css2?family=Marcellus&display=swap">
<style>
  :root {
    --backdrop: #2a2522;
    --card: #050505;
    --ink: #f2f2f2;
    --accent: #c0182f;
    --muted: #9aa0a6;
    --net-light: #3c4046;
  }
  * { box-sizing: border-box; margin: 0; padding: 0; }
  html, body { width: 1200px; height: 900px; overflow: hidden; }
  body {
    background: var(--backdrop);
    font-family: "Marcellus", "Optima", serif;
    color: var(--ink);
    position: relative;
  }
  .card {
    position: absolute;
    left: 270px;
    width: 660px;
    height: 377px;
    background: var(--card);
    border-radius: 30px;
    overflow: hidden;
  }
  .card--front { top: 48px; }
  .card--back { top: 475px; }

  .wordmark {
    display: flex;
    align-items: center;
    gap: 10px;
    color: var(--ink);
    letter-spacing: 0.18em;
  }
  .wordmark__dot {
    width: 10px; height: 10px;
    border-radius: 50%;
    background: var(--accent);
  }
  .card--front .wordmark {
    position: absolute;
    left: 50%; top: 50%;
    transform: translate(-50%, -50%);
    font-size: 64px;
  }

  .network {
    position: absolute;
    right: 0; top: 0;
    width: 360px; height: 100%;
    background:
      radial-gradient(ellipse at 70% 35%, var(--net-light) 0%, #1a1c1f 45%, transparent 75%),
      linear-gradient(100deg, var(--card) 0%, #101113 40%, #1e2024 100%);
  }

  .contact {
    position: absolute;
    left: 40px; top: 42px;
    width: 330px;
  }
  .contact__name { color: var(--accent); font-size: 25px; line-height: 1.1; }
  .contact__role { font-size: 17px; margin-top: 4px; }
  .contact__list { list-style: none; margin-top: 20px; }
  .contact__item {
    display: flex; align-items: center; gap: 10px;
    font-size: 16px; line-height: 1.7;
  }
  .contact__item svg { width: 14px; height: 14px; fill: var(--accent); flex: none; }
  .contact__rule {
    margin-top: 16px;
    height: 1px;
    background: var(--accent);
  }
  .card--back .wordmark {
    position: absolute;
    left: 110px; top: 262px;
    font-size: 46px;
  }

  .address {
    position: absolute;
    right: 40px; bottom: 42px;
    text-align: right;
    font-size: 16px; line-height: 1.35;
  }
  .address__line { display: flex; justify-content: flex-end; align-items: center; gap: 6px; }
  .address svg { width: 13px; height: 16px; fill: var(--accent); }
</style>
</head>
<body>

<section class="card card--front" aria-label="Card front">
  <div class="wordmark"><span>QORLIN</span><span class="wordmark__dot"></span></div>
</section>

<section class="card card--back" aria-label="Card back">
  <div class="network" role="img" aria-label="Abstract network of connected dots and lines"></div>

  <div class="contact">
    <p class="contact__name">Marcello Bianchi</p>
    <p class="contact__role">Co-Founder &amp; CEO - QORLIN Research</p>
    <ul class="contact__list">
      <li class="contact__item">
        <svg viewBox="0 0 24 24" aria-hidden="true"><path d="M6.6 10.8a15.1 15.1 0 0 0 6.6 6.6l2.2-2.2c.3-.3.7-.4 1-.2 1.1.4 2.3.6 3.6.6.6 0 1 .4 1 1V20c0 .6-.4 1-1 1A17 17 0 0 1 3 4c0-.6.4-1 1-1h3.5c.6 0 1 .4 1 1 0 1.3.2 2.5.6 3.6.1.3 0 .7-.2 1z"/></svg>
        604318275
      </li>
      <li class="contact__item">
        <svg viewBox="0 0 24 24" aria-hidden="true"><path d="M2 5h20v14H2zm2 2v.5l8 5 8-5V7l-8 5z"/></svg>
        info@qorlin-analytics.example
      </li>
      <li class="contact__item">
        <svg viewBox="0 0 24 24" aria-hidden="true"><path d="M12 2a10 10 0 1 0 0 20 10 10 0 0 0 0-20zm6.9 6h-3a15 15 0 0 0-1.3-3.9A8 8 0 0 1 18.9 8zM12 4c.8 1.2 1.5 2.5 1.9 4h-3.8c.4-1.5 1.1-2.8 1.9-4zM4.3 14a8 8 0 0 1 0-4h3.4a16 16 0 0 0 0 4zm.8 2h3a15 15 0 0 0 1.3 3.9A8 8 0 0 1 5.1 16zM8 8H5a8 8 0 0 1 4.4-3.9C8.8 5.3 8.4 6.6 8 8zm4 12c-.8-1.2-1.5-2.5-1.9-4h3.8c-.4 1.5-1.1 2.8-1.9 4zm2.3-6H9.7a14 14 0 0 1 0-4h4.6a14 14 0 0 1 0 4zm.3 5.9c.6-1.2 1-2.5 1.4-3.9h3a8 8 0 0 1-4.4 3.9zm1.7-5.9a16 16 0 0 0 0-4h3.4a8 8 0 0 1 0 4z"/></svg>
        www.qorlin-analytics.example
      </li>
    </ul>
    <div class="contact__rule"></div>
  </div>

  <div class="wordmark"><span>QORLIN</span><span class="wordmark__dot"></span></div>

  <address class="address" style="font-style: normal;">
    <span class="address__line">48 rue des Lilas
      <svg viewBox="0 0 24 30" aria-hidden="true"><path d="M12 0a10 10 0 0 0-10 10c0 7.5 10 20 10 20s10-12.5 10-20A10 10 0 0 0 12 0zm0 14a4 4 0 1 1 0-8 4 4 0 0 1 0 8z"/></svg>
    </span>
    <span class="address__line">75012 Paris</span>
  </address>
</section>

</body>
</html>
```